Business Card Design Project

Need a business card design for a new company called StoneWave.

We help large data center customers optimize and transform their data centers.

We have't gotten a logo yet but are in the process of running a separate contest to do that here on ArtHive.

Will post the logo shortly.
Updates

Project Deadline Extended
Reason: Not sure why this came up as a deadline of November 3d. We just launched it today. Going to send an email to ArtHive

Just uploaded larger files of the logo

Target Market(s)

Our target customers of our business are organizations with large data centers looking at optimizing their current data centers, relocating or consolidating their data centers into new data centers.

Typically our buyer will be the CIO, CTO or CFO of the organization.

Industry/Entity Type

Business

Font styles to use
Sans Serif

Colors
3276b5
fece3e

Requirements
Nice to have
• Be readable by the business card reader.
Should not have
• Small type that can't be scanned or easily read
Odd shape or size

```html
<!DOCTYPE html>
<html lang="en">
<head>
<meta charset="utf-8">
<title>StoneWave Business Card</title>
<link rel="stylesheet" href="https://fonts.googleapis.com/css2?family=Arimo:wght@400;700&display=swap">
<style>
  :root {
    --page-bg: #ffffff;
    --card-dark: #202326;
    --card-light: #ffffff;
    --card-border: #9a9a9a;
    --brand-blue: #2f8fc4;
    --brand-orange: #e8843a;
    --text-dark: #2b2b2b;
    --text-muted: #8a8a8a;
  }
  * { margin: 0; padding: 0; box-sizing: border-box; }
  html, body {
    width: 1200px; height: 900px; overflow: hidden;
    background: var(--page-bg);
    font-family: "Arimo", Arial, sans-serif;
  }
  .canvas { position: relative; width: 1200px; height: 900px; }

  .card { position: absolute; left: 219px; width: 762px; height: 429px; }
  .card--front { top: 11px; background: var(--card-dark); }
  .card--back { top: 459px; background: var(--card-light); border: 1px solid var(--card-border); }

  .brand { position: absolute; display: flex; align-items: center; }
  .brand__mark { border-radius: 50%; background: var(--brand-orange); flex: none; }
  .brand__name { color: var(--brand-blue); font-weight: 400; letter-spacing: -0.5px; }

  .card--front .brand { left: 140px; top: 167px; }
  .card--front .brand__mark { width: 110px; height: 110px; margin-right: 28px; }
  .card--front .brand__name { font-size: 64px; }

  .card--back .brand { left: 392px; top: 66px; }
  .card--back .brand__mark { width: 72px; height: 72px; margin-right: 18px; }
  .card--back .brand__name { font-size: 44px; }

  .person { position: absolute; left: 53px; top: 165px; }
  .person__name { color: var(--brand-blue); font-weight: 700; font-size: 28px; line-height: 34px; }
  .person__role { color: var(--text-muted); font-size: 19px; line-height: 26px; }

  .contact-list, .address { position: absolute; list-style: none; }
  .contact-list { left: 53px; top: 253px; }
  .contact-list li, .address li {
    display: flex; align-items: center;
    height: 29.5px; font-size: 24px; color: var(--text-dark);
  }
  .icon { width: 24px; height: 24px; margin-right: 18px; flex: none; fill: var(--brand-blue); }

  .address { left: 378px; top: 253px; }
  .address__pin { position: absolute; left: -4px; top: 0; width: 22px; height: 32px; fill: var(--brand-blue); }
  .address li { padding-left: 37px; }
</style>
</head>
<body>
<main class="canvas">
  <section class="card card--front">
    <div class="brand">
      <span class="brand__mark"></span>
      <span class="brand__name">StoneWave</span>
    </div>
  </section>

  <section class="card card--back">
    <div class="brand">
      <span class="brand__mark"></span>
      <span class="brand__name">StoneWave</span>
    </div>

    <div class="person">
      <p class="person__name">Person Name</p>
      <p class="person__role">Designation</p>
    </div>

    <ul class="contact-list">
      <li>
        <svg class="icon" viewBox="0 0 24 24" aria-hidden="true"><path d="M2 11c0-4 4.5-6 10-6s10 2 10 6l-1 2h-4l-1-3H8l-1 3H3z"/><path d="M6 14h12l2 5H4z"/><circle cx="12" cy="16.5" r="1.6" fill="#fff"/></svg>
        <span>900 3000 5000</span>
      </li>
      <li>
        <svg class="icon" viewBox="0 0 24 24" aria-hidden="true"><path d="M7 1h10a2 2 0 0 1 2 2v18a2 2 0 0 1-2 2H7a2 2 0 0 1-2-2V3a2 2 0 0 1 2-2zm0 3v14h10V4z"/><circle cx="12" cy="20.5" r="1.2" fill="#fff"/></svg>
        <span>000 3000 5000</span>
      </li>
      <li>
        <svg class="icon" viewBox="0 0 24 24" aria-hidden="true"><path d="M1 5h22v14H1z"/><path d="M1 5l11 8 11-8M1 19l8-7M23 19l-8-7" fill="none" stroke="#fff" stroke-width="1.4"/></svg>
        <span>info@stonewave.com</span>
      </li>
      <li>
        <svg class="icon" viewBox="0 0 24 24" aria-hidden="true" fill="none" style="fill:none;stroke:var(--brand-blue);stroke-width:2"><circle cx="12" cy="12" r="9"/><ellipse cx="12" cy="12" rx="4" ry="9"/><path d="M3 12h18"/></svg>
        <span>www.stonewave.com</span>
      </li>
    </ul>

    <div class="address">
      <svg class="address__pin" viewBox="0 0 22 32" aria-hidden="true"><path d="M11 0a10 10 0 0 1 10 10c0 7-10 22-10 22S1 17 1 10A10 10 0 0 1 11 0z"/><circle cx="11" cy="10" r="4" fill="#fff"/></svg>
      <ul>
        <li>Address will come here</li>
        <li>Address will come here</li>
        <li>Address will come here</li>
      </ul>
    </div>
  </section>
</main>
</body>
</html>
```